High-end Investment firm website

It needs to feel very high-end. We like clean design which incorporates a good deal of white space with the use of imagery to be provided.

Here are a few examples of design which is appealing:
https://www.corlandholdings.example
https://www.brevikcapital.example

Please use the following shade of blue in the design #7BAFD4.

Additional brand colors black, grey and white.

This google doc has a link to all of the content for the site. It also has detailed design notes per section.

https://files.quenderpad.example/doc/7TRaM2pLwe9XnqBv4KcYh0sJd8FgU3oZi5EtNm1Qx/edit?usp=sharing

Target Market(s)

Investors and companies in our target industries

Industry/Entity Type

Investment

Coding

Coded - Design and coding required

Number of Pages Required

5+ page

Font styles to use
Sans Serif

Requirements
Must have
• Clean feel, lots of white space.
Nice to have
• Clean graphics similar to https://www.corlandholdings.example

```html
<!DOCTYPE html>
<html lang="en">
<head>
<meta charset="utf-8">
<title>Meridane Holdings</title>
<link rel="stylesheet" href="https://fonts.googleapis.com/css2?family=Lato:wght@300;400;700&display=swap">
<style>
:root{
  --brand-blue:#7bafd4;
  --band-blue:#6a9fcf;
  --deep-blue:#2b4f86;
  --ink:#1f1f1f;
  --text:#333333;
  --grey-bg:#eeeeee;
  --footer:#232323;
  --navy:#111a2c;
  --white:#ffffff;
}
*{box-sizing:border-box;margin:0;padding:0}
html,body{width:1200px;height:4053px;overflow:hidden}
body{position:relative;font-family:'Lato',sans-serif;color:var(--text);background:var(--white)}
section,header,footer{position:absolute;left:0;width:1200px}
.abs{position:absolute}

/* hero */
.hero{top:0;height:761px;background:linear-gradient(135deg,#4a6fa6 0%,#5b85bd 45%,#3f6aa8 70%,#2e5590 100%)}
.hero-photo{position:absolute;inset:0;background:linear-gradient(120deg,rgba(40,70,130,.55) 0%,rgba(110,150,200,.35) 55%,rgba(70,105,160,.5) 100%)}
.brand{position:absolute;left:75px;top:60px;width:152px;text-align:center;color:var(--white)}
.brand-name{font-size:23px;letter-spacing:1px;font-weight:400}
.brand-sub{font-size:9px;letter-spacing:4px;margin-top:2px;border-top:1px solid currentColor;padding-top:3px}
.main-nav a{position:absolute;top:72px;color:var(--white);font-size:14px;font-weight:700;text-decoration:none;letter-spacing:.3px;white-space:nowrap}
.main-nav a.active::after{content:"";position:absolute;left:-8px;right:-8px;top:26px;height:2px;background:var(--ink)}
.hero-title{position:absolute;left:75px;top:484px;color:var(--white);font-size:41px;font-weight:300;line-height:46px;letter-spacing:.5px}

/* about */
.about{top:761px;height:519px}
.eyebrow{left:75px;top:100px;color:var(--brand-blue);font-size:15px;font-weight:700;line-height:18px}
.section-title{font-size:52px;font-weight:300;color:var(--ink);letter-spacing:1px;line-height:1.1;white-space:nowrap}
.about .section-title{left:75px;top:123px}
.about-copy{left:75px;top:188px;width:560px;font-size:15px;line-height:29.5px;color:var(--ink)}
.btn-outline{left:75px;top:367px;width:164px;height:49px;border:2px solid var(--brand-blue);color:var(--ink);font-size:15px;display:flex;align-items:center;justify-content:center;letter-spacing:.5px}
.about-visual{left:670px;top:38px;width:456px;height:450px;background:linear-gradient(160deg,#1c2d55 0%,#2c5aa0 50%,#142244 100%)}

/* focus */
.focus{top:1280px;height:369px;background:var(--band-blue)}
.focus .section-title{width:100%;text-align:center;top:66px;color:var(--white)}
.focus-item{position:absolute;top:152px;width:200px;margin-left:-100px;text-align:center;color:var(--white);font-size:18px;font-weight:700;line-height:26px}
.focus-item svg{display:block;margin:0 auto 18px;width:76px;height:76px}

/* capital */
.capital{top:1649px;height:518px}
.capital-copy{left:75px;top:96px;width:505px;font-size:35px;font-weight:300;line-height:45px;color:var(--ink)}
.capital-visual{left:615px;top:0;width:585px;height:518px;background:linear-gradient(135deg,#6f6f6f 0%,#9a9a9a 45%,#6e8b4e 70%,#5b5b5b 100%)}

/* experience */
.experience{top:2167px;height:559px;background:var(--grey-bg)}
.experience .section-title{width:100%;text-align:center;top:68px}
.experience-lede{width:100%;text-align:center;top:156px;font-size:15px;color:var(--ink)}
.portfolio-tile{position:absolute;width:242px;height:88px;background:var(--white);display:flex;align-items:center;justify-content:center;gap:10px;font-size:24px;font-weight:700;color:#1f3d7a}
.portfolio-tile .mark{width:16px;height:16px;border-radius:50%;background:var(--brand-blue)}
.portfolio-tile.small{font-size:14px;font-weight:400}
.dot{position:absolute;width:12px;height:12px;border-radius:50%;background:#333}
.dot.on{background:var(--brand-blue)}

/* team */
.team{top:2726px;height:609px}
.team .section-title{width:100%;text-align:center;top:52px}
.team-card{left:75px;top:148px;width:1051px;height:395px;border:2px solid var(--brand-blue);background:linear-gradient(90deg,#ffffff 0%,#ffffff 50%,#b9bcc2 75%,#8f939a 100%)}
.team-photo{right:0;top:0;width:420px;height:391px;background:linear-gradient(90deg,rgba(255,255,255,0) 0%,rgba(60,64,72,.35) 60%,rgba(40,44,52,.55) 100%)}
.team-bio{left:22px;top:33px;width:545px;font-size:15px;line-height:34px;color:var(--ink)}
.team-role{left:22px;top:292px;font-size:15px;font-weight:700;color:var(--brand-blue)}
.team-card .dot{top:342px}

/* contact */
.contact{top:3335px;height:519px;background:var(--band-blue)}
.contact-visual{left:0;top:0;width:585px;height:519px;background:linear-gradient(180deg,#e39a64 0%,#c97a55 35%,#4b4a55 70%,#2a2a33 100%)}
.contact .section-title{left:614px;top:70px;color:var(--white)}
.field{position:absolute;height:46px;border:1px solid rgba(255,255,255,.8);color:var(--white);font-size:12px;font-weight:700;padding:15px 16px}
.submit{left:615px;top:393px;width:151px;height:46px;background:var(--navy);color:var(--white);font-size:17px;font-weight:700;display:flex;align-items:center;justify-content:center;letter-spacing:.5px}

/* footer */
.site-footer{top:3854px;height:199px;background:var(--footer)}
.site-footer .brand{top:60px;color:var(--brand-blue)}
.copyright{left:253px;top:96px;font-size:12px;line-height:25px;color:#9a9a9a}
.footer-nav a{position:absolute;top:82px;color:var(--white);font-size:13px;font-weight:700;text-decoration:none;white-space:nowrap}
.social{position:absolute;top:123px;width:20px;height:20px;border-radius:50%;background:var(--white)}
</style>
</head>
<body>

<header class="hero">
  <div class="hero-photo" role="img" aria-label="Robotic arms on an automated factory line under a blue tint"></div>
  <div class="brand"><div class="brand-name">MERIDANE</div><div class="brand-sub">HOLDINGS</div></div>
  <nav class="main-nav">
    <a class="active" href="#" style="left:421px">HOME</a>
    <a href="#" style="left:520px">ABOUT US</a>
    <a href="#" style="left:648px">INVESTMENT FOCUS</a>
    <a href="#" style="left:849px">INDUSTRY FOCUS</a>
    <a href="#" style="left:1032px">CONTACT US</a>
  </nav>
  <h1 class="hero-title">Partnering with<br>Exceptional Leaders Building<br>World-Class Companies</h1>
</header>

<section class="about">
  <p class="abs eyebrow">WHO WE ARE</p>
  <h2 class="abs section-title">ABOUT US</h2>
  <p class="abs about-copy">Meridane Holdings focuses on opportunities where it can support senior management to drive rapid growth and profit improvement through capital infusion, technology innovation and organizational expertise.<br>We invest across a variety of growth industries with an emphasis on reshoring and rebuilding America.</p>
  <a class="abs btn-outline">READ MORE</a>
  <div class="abs about-visual" role="img" aria-label="Night city skyline with glowing data lines"></div>
</section>

<section class="focus">
  <h2 class="abs section-title">AREAS OF FOCUS</h2>
  <div class="focus-item" style="left:170px">
    <svg viewBox="0 0 76 76" fill="none" stroke="#1f1f1f" stroke-width="2.5"><path d="M38 6 L64 16 L62 44 Q56 62 38 70 Q20 62 14 44 L12 16 Z"/><circle cx="38" cy="38" r="16"/><path d="M38 27 L41 35 L49 35 L43 40 L45 48 L38 43 L31 48 L33 40 L27 35 L35 35 Z"/></svg>
    Defense</div>
  <div class="focus-item" style="left:385px">
    <svg viewBox="0 0 76 76" fill="none" stroke="#1f1f1f" stroke-width="2.5"><rect x="8" y="14" width="60" height="40" rx="2"/><path d="M30 54 L28 66 M46 54 L48 66 M22 66 H54"/><rect x="29" y="32" width="18" height="14"/><path d="M32 32 V26 a6 6 0 0 1 12 0 V32"/></svg>
    Cyber Security</div>
  <div class="focus-item" style="left:599px">
    <svg viewBox="0 0 76 76" fill="none" stroke="#1f1f1f" stroke-width="2.5"><path d="M6 68 V10 H14 V36 L28 28 V36 L42 28 V36 L56 28 V36 H70 V68 Z"/><path d="M20 10 V36 M14 50 H62 M14 58 H62"/><rect x="20" y="42" width="10" height="6"/><rect x="46" y="42" width="10" height="6"/></svg>
    Industrials</div>
  <div class="focus-item" style="left:815px">
    <svg viewBox="0 0 76 76" fill="none" stroke="#1f1f1f" stroke-width="2.5"><rect x="18" y="6" width="40" height="36"/><path d="M26 14 H50 M26 22 H50 M26 30 H50"/><circle cx="38" cy="54" r="14"/><circle cx="38" cy="54" r="5"/><path d="M8 50 H24 M52 50 H68"/></svg>
    Digital Enterprise</div>
  <div class="focus-item" style="left:1029px">
    <svg viewBox="0 0 76 76" fill="none" stroke="#1f1f1f" stroke-width="2.5"><circle cx="38" cy="38" r="24"/><circle cx="38" cy="38" r="16"/><circle cx="38" cy="38" r="6"/><path d="M38 8 V14 M38 62 V68 M8 38 H14 M62 38 H68 M17 17 L21 21 M55 55 L59 59 M59 17 L55 21 M21 55 L17 59"/></svg>
    Technology and<br>Professional</div>
</section>

<section class="capital">
  <p class="abs capital-copy">We place capital for long-term growth and revenue generation. Our investment horizon enables a focus on building strong sustainable companies, with empowered teams maximizing impact.</p>
  <div class="abs capital-visual" role="img" aria-label="Hand watering a potted plant growing in the shape of a rising chart"></div>
</section>

<section class="experience">
  <h2 class="abs section-title">INVESTMENT EXPERIENCE</h2>
  <p class="abs experience-lede">The Meridane Holdings team has invested in, managed and served on the boards of a variety of high performing companies.</p>
  <div class="portfolio-tile small" style="left:75px;top:215px">Larchmont Capital Partners</div>
  <div class="portfolio-tile" style="left:346px;top:215px"><span class="mark"></span>Quillon AI</div>
  <div class="portfolio-tile" style="left:615px;top:215px">Tallyform</div>
  <div class="portfolio-tile" style="left:884px;top:215px"><span class="mark"></span>Verano Capital</div>
  <div class="portfolio-tile" style="left:212px;top:333px">StakeGrid</div>
  <div class="portfolio-tile" style="left:481px;top:333px">Harbor Loft</div>
  <div class="portfolio-tile" style="left:752px;top:333px"><span class="mark"></span>Crestline Row</div>
  <span class="dot on" style="left:556px;top:467px"></span>
  <span class="dot" style="left:581px;top:467px"></span>
  <span class="dot" style="left:606px;top:467px"></span>
  <span class="dot" style="left:631px;top:467px"></span>
</section>

<section class="team">
  <h2 class="abs section-title">MANAGEMENT TEAM</h2>
  <div class="abs team-card">
    <div class="abs team-photo" role="img" aria-label="Portrait of a partner in a dark suit and striped tie"></div>
    <p class="abs team-bio">Jonathan Halverson is a Partner at Meridane Holdings, where he serves on the investment committee and plays a key role in devising strategies which enhance the operational efficiencies of portfolio companies.<br>He additionally serves as the Founding Partner of the single family office and advisory firm Halverson Capital. Within Halverson Capital he serves on the investment committee, and works closely with portfolio companies across the media, tech, education, aviation, and real estate industries</p>
    <p class="abs team-role">Jonathan Halverson is a Partner</p>
    <span class="dot" style="left:26px"></span>
    <span class="dot on" style="left:53px"></span>
    <span class="dot on" style="left:79px"></span>
    <span class="dot on" style="left:106px"></span>
  </div>
</section>

<section class="contact">
  <div class="abs contact-visual" role="img" aria-label="City skyline with a tall spire at sunset"></div>
  <h2 class="abs section-title">CONTACT US</h2>
  <div class="field" style="left:615px;top:156px;width:252px">NAME</div>
  <div class="field" style="left:876px;top:156px;width:250px">PHONE NO</div>
  <div class="field" style="left:615px;top:214px;width:511px">EMAIL ADDRESS</div>
  <div class="field" style="left:615px;top:274px;width:511px;height:104px">MESSAGE</div>
  <div class="abs submit">SUBMIT</div>
</section>

<footer class="site-footer">
  <div class="brand"><div class="brand-name">MERIDANE</div><div class="brand-sub">HOLDINGS</div></div>
  <p class="abs copyright">Copyright © 2020. Company Name.<br>All Right Reserved</p>
  <nav class="footer-nav">
    <a href="#" style="left:544px">HOME</a>
    <a href="#" style="left:623px">ABOUT US</a>
    <a href="#" style="left:725px">INVESTMENT FOCUS</a>
    <a href="#" style="left:894px">INDUSTRY FOCUS</a>
    <a href="#" style="left:1044px">CONTACT US</a>
  </nav>
  <span class="social" style="left:924px" aria-label="Social link"></span>
  <span class="social" style="left:967px" aria-label="Social link"></span>
  <span class="social" style="left:1014px" aria-label="Social link"></span>
  <span class="social" style="left:1060px" aria-label="Social link"></span>
  <span class="social" style="left:1105px" aria-label="Social link"></span>
</footer>

</body>
</html>
```